We need a flyer designed for our 4th Annual Harvestlight: A Kinfolk Gathering of Heritage Festival that includes the day, time, location, address, and logos. It also needs to include what to expect. The event will be held on Saturday June 14th from 12p-6p at Gallery Commons located at 418 N. Belcourt Ave., Pensacola, FL 32507. Please see uploaded files for prior flyers for reference when it comes to information to include. Also I've uploaded pictures from our prior festivals that you may incorporate and logos.

```html
<!DOCTYPE html>
<html lang="en">
<head>
<meta charset="utf-8">
<title>4th Annual Harvestlight Festival Flyer</title>
<link href="https://fonts.googleapis.com/css2?family=Alfa+Slab+One&family=Anton&family=Bowlby+One&family=Kaushan+Script&family=Montserrat:wght@500;600;700;800&family=Oswald:wght@600;700&display=swap" rel="stylesheet">
<style>
  :root {
    --orange: #f5a623;
    --red: #e8322b;
    --green: #3aa935;
    --yellow: #ffe11a;
    --black: #121212;
    --white: #ffffff;
    --ink: #1c1c1c;
  }
  * { box-sizing: border-box; margin: 0; padding: 0; }
  html, body { width: 841px; height: 1200px; overflow: hidden; background: var(--white); }
  .flyer { position: relative; width: 841px; height: 1200px; overflow: hidden; background: var(--orange); font-family: "Montserrat", sans-serif; }
  .layer { position: absolute; left: 0; top: 0; width: 841px; height: 1200px; }
  .abs { position: absolute; }

  .hero-photo { left: 0; top: 0; width: 841px; height: 467px;
    background: linear-gradient(180deg, #7fb8e6 0%, #b9d3e6 28%, #c8a77c 42%, #6f8f48 62%, #c94a3a 72%, #e9c845 78%, #dfe3e6 86%, #6d9a3c 100%);
    clip-path: polygon(525px 0, 841px 0, 841px 467px, 0 467px, 0 300px); }

  .brand { left: 18px; top: 30px; display: flex; align-items: center; gap: 10px; }
  .brand-dot { width: 34px; height: 34px; border-radius: 50%; background: var(--orange); }
  .brand-name { font-weight: 700; font-size: 17px; color: var(--ink); letter-spacing: .5px; }
  .presents { left: 20px; top: 100px; font-weight: 600; font-size: 20px; letter-spacing: 6px; color: var(--red); }

  .title-banner { left: -45px; top: 111px; width: 620px; height: 58px; background: var(--red);
    transform: rotate(-28deg); display: flex; align-items: center; justify-content: center; white-space: nowrap;
    font-family: "Oswald", sans-serif; font-weight: 700; font-size: 36px; color: var(--white); letter-spacing: .5px; }

  .free-badge { left: 640px; top: 50px; width: 170px; transform: rotate(-4deg); text-align: center; }
  .free-badge .big { font-family: "Bowlby One", sans-serif; font-size: 40px; line-height: 40px; color: var(--yellow); }
  .free-badge .small { font-weight: 800; font-size: 14px; line-height: 16px; color: var(--white); margin-top: 4px; }

  .tagline-band { left: 0; top: 467px; width: 841px; height: 45px; background: var(--red);
    clip-path: polygon(175px 0, 841px 0, 841px 45px, 150px 45px);
    display: flex; align-items: center; justify-content: flex-end; padding-right: 36px;
    font-weight: 600; font-size: 23px; color: var(--white); letter-spacing: .5px; }

  .invite { left: 270px; top: 518px; width: 540px; text-align: center; white-space: nowrap; }
  .invite .script { font-family: "Kaushan Script", cursive; font-size: 34px; color: var(--ink);
    text-shadow: 2px 2px 0 var(--white); line-height: 46px; }
  .invite .headline { font-family: "Alfa Slab One", serif; font-size: 30px; color: var(--white); line-height: 40px;
    text-shadow: 2px 2px 0 var(--red), -1px -1px 0 var(--red); letter-spacing: 1px; }

  .card { border: 7px solid var(--white); box-shadow: 0 0 0 3px var(--red); }
  .card-community { left: 30px; top: 612px; width: 280px; height: 168px; transform: rotate(5deg);
    background: linear-gradient(180deg, #a9c9e0 0%, #6e9a4e 40%, #c9b9a4 70%, #c0503c 100%); }
  .card-arts { left: 292px; top: 626px; width: 266px; height: 160px; box-shadow: 0 0 0 3px var(--red);
    background: linear-gradient(180deg, #7fa3c2 0%, #5e8a3f 35%, #7a4c9c 60%, #6b6b3c 100%); }
  .card-culture { left: 520px; top: 670px; width: 280px; height: 176px; transform: rotate(-5deg);
    background: linear-gradient(180deg, #2a2a2a 0%, #5b3a2c 35%, #6d7a3e 60%, #8a4a2a 100%); }
  .label { font-family: "Alfa Slab One", serif; color: var(--red); text-shadow: 1px 1px 0 var(--white); white-space: nowrap; }
  .label-community { left: 38px; top: 570px; font-size: 24px; transform: rotate(8deg); }
  .label-arts { left: 392px; top: 789px; font-size: 22px; }
  .label-culture { left: 806px; top: 800px; font-size: 22px; transform: rotate(-90deg); transform-origin: left top; }

  .date { left: 40px; top: 796px; display: flex; align-items: flex-start; }
  .date .day { font-family: "Alfa Slab One", serif; font-size: 26px; color: var(--green); transform: rotate(-90deg);
    width: 34px; margin-top: 48px; }
  .date .num { font-family: "Anton", sans-serif; font-size: 100px; line-height: 104px; color: var(--red); margin-left: 4px; }
  .date .month { font-family: "Kaushan Script", cursive; font-size: 56px; color: var(--white); line-height: 60px; margin-left: 8px; }
  .time { left: 176px; top: 878px; font-family: "Alfa Slab One", serif; font-size: 21px; color: var(--ink); }

  .venue { left: 14px; top: 922px; display: flex; gap: 12px; }
  .venue svg { flex: none; }
  .venue-name { font-weight: 600; font-size: 24px; color: var(--ink); letter-spacing: .5px; }
  .venue-address { font-weight: 600; font-size: 16px; line-height: 21px; color: var(--ink); }

  .crowd-photo { left: 0; top: 1009px; width: 305px; height: 191px;
    clip-path: polygon(0 0, 290px 0, 305px 191px, 0 191px);
    background: linear-gradient(160deg, #7c9a48 0%, #b6c58c 35%, #f1eee6 60%, #d8663a 100%); }

  .bring-badge { left: 292px; top: 965px; width: 136px; height: 136px; border-radius: 50%;
    background: var(--red); border: 6px solid var(--black); box-shadow: 0 0 0 3px var(--white);
    display: flex; align-items: center; justify-content: center; text-align: center;
    font-weight: 700; font-size: 13px; line-height: 15px; color: var(--white); }

  .expect-box { left: 404px; top: 945px; width: 415px; height: 186px; background: var(--green); }
  .expect-ribbon { left: 430px; top: 918px; width: 240px; height: 46px; background: var(--red); transform: rotate(-14deg);
    display: flex; align-items: center; justify-content: center; font-weight: 700; font-size: 24px; color: var(--white); }
  .expect-list { left: 404px; top: 1012px; width: 415px; list-style: none; text-align: center;
    font-weight: 600; font-size: 14.5px; line-height: 18px; color: var(--white); }

  .footer { left: 335px; top: 1162px; width: 490px; display: flex; align-items: center; justify-content: space-between; }
  .firm { display: flex; align-items: center; gap: 8px; font-weight: 700; font-size: 13px; color: var(--white); }
  .firm-square { width: 18px; height: 18px; background: var(--yellow); }
  .website { font-weight: 700; font-size: 15px; color: var(--yellow); }
</style>
</head>
<body>
<main class="flyer">
  <svg class="layer" viewBox="0 0 841 1200" aria-hidden="true">
    <polygon points="0,0 560,0 0,320" fill="var(--white)"/>
    <polygon points="620,690 841,640 841,1200 303,1200 330,990 560,880" fill="var(--black)"/>
    <polygon points="400,930 700,880 712,912 396,970" fill="var(--green)"/>
  </svg>

  <div class="abs hero-photo" role="img" aria-label="Photo of giant light-up festival letters with a red, yellow, green and black balloon arch on a park lawn in front of a museum building"></div>

  <svg class="layer" viewBox="0 0 841 1200" aria-hidden="true">
    <polygon points="798,235 841,225 841,462 798,462" fill="var(--orange)"/>
    <g fill="none" stroke="var(--red)" stroke-width="3">
      <circle cx="818" cy="262" r="13"/><circle cx="818" cy="262" r="5"/>
      <circle cx="818" cy="300" r="13"/><circle cx="818" cy="300" r="5"/>
      <circle cx="822" cy="368" r="11"/><circle cx="822" cy="368" r="4"/>
      <circle cx="822" cy="398" r="11"/><circle cx="822" cy="398" r="4"/>
      <circle cx="822" cy="428" r="11"/><circle cx="822" cy="428" r="4"/>
    </g>
    <polygon points="645,62 841,22 841,210 690,262" fill="var(--red)"/>
    <polygon points="630,46 806,18 820,214 668,250" fill="var(--green)"/>
    <g stroke="var(--white)" stroke-width="4" stroke-linecap="round">
      <line x1="600" y1="72" x2="622" y2="80"/>
      <line x1="602" y1="104" x2="624" y2="100"/>
      <line x1="606" y1="44" x2="624" y2="60"/>
      <line x1="630" y1="20" x2="640" y2="40"/>
      <line x1="660" y1="10" x2="664" y2="30"/>
      <line x1="608" y1="132" x2="626" y2="122"/>
    </g>
    <polygon points="100,488 152,512 100,538" fill="var(--white)"/>
    <polygon points="4,496 50,518 8,552" fill="none" stroke="var(--white)" stroke-width="4"/>
    <polygon points="766,938 841,870 841,938" fill="var(--red)"/>
    <polygon points="744,980 790,1004 744,1028" fill="var(--white)"/>
  </svg>

  <div class="abs brand"><span class="brand-dot"></span><span class="brand-name">The Marlowe Kin Foundation</span></div>
  <div class="abs presents">PRESENTS</div>
  <div class="abs title-banner">THE 4TH ANNUAL HARVESTLIGHT</div>

  <div class="abs free-badge">
    <div class="big">FREE</div>
    <div class="big">EVENT!</div>
    <div class="small">EVERYONE<br>ARE WELCOME</div>
  </div>

  <div class="abs tagline-band">A KINFOLK GATHERING OF HERITAGE</div>

  <div class="abs invite">
    <div class="script">Come and Join Us for A Day of</div>
    <div class="headline">FREEDOM CELEBRATION</div>
  </div>

  <div class="abs card card-community" role="img" aria-label="Photo of festival guests walking among vendor tents"></div>
  <div class="abs card card-arts" role="img" aria-label="Photo of a youth dance troupe performing on the lawn"></div>
  <div class="abs card card-culture" role="img" aria-label="Photo of drummers in traditional attire playing hand drums"></div>
  <div class="abs label label-community">COMMUNITY</div>
  <div class="abs label label-arts">ARTS</div>
  <div class="abs label label-culture">CULTURE</div>

  <div class="abs date">
    <span class="day">SAT</span>
    <span class="num">14</span>
    <span class="month">June</span>
  </div>
  <div class="abs time">12 PM-6 PM</div>

  <div class="abs venue">
    <svg width="40" height="62" viewBox="0 0 40 62" aria-hidden="true">
      <path d="M20 60 C20 60 2 34 2 20 A18 18 0 0 1 38 20 C38 34 20 60 20 60 Z" fill="var(--red)"/>
      <circle cx="20" cy="20" r="9" fill="var(--orange)"/>
    </svg>
    <div>
      <div class="venue-name">GALLERY COMMONS</div>
      <div class="venue-address">418 N. Belcourt Ave.<br>Pensacola, FL 32507</div>
    </div>
  </div>

  <div class="abs crowd-photo" role="img" aria-label="Photo of festival choir members in matching white shirts singing and clapping"></div>

  <div class="abs bring-badge">BRING<br>YOUR OWN<br>CHAIRS &amp;<br>PICNIC<br>BLANKET!</div>

  <div class="abs expect-box"></div>
  <div class="abs expect-ribbon">What to Expect</div>
  <ul class="abs expect-list">
    <li>LIVE PERFORMANCES</li>
    <li>FOOD VENDORS</li>
    <li>ART / AFRICAN CLOTHING VENDORS</li>
    <li>KIDS OBSTACLE COURSE &amp; PLAY AREA</li>
    <li>SPADES &amp; DOMINO TABLES</li>
  </ul>

  <div class="abs footer">
    <span class="firm"><span class="firm-square"></span>The Marlowe Firm, PLLC</span>
    <span class="website">MARLOWEKINFOUNDATION.ORG</span>
  </div>
</main>
</body>
</html>
```